Qasemir Institiute Australia needs a book cover design

Design book cover (front and back) for upcoming publication called "Lanterns & Pathways of Dawn"

Target Market(s)

Religious, Academic & Philosophical

Colors
0094D4
00A9DD
6FCCEA
C7EBF8
E9F6FB

Requirements
Must have
• Some essential attributes on the book cover, author's name (Ayatollah Karim Masoudeh)
Nice to have
• Islamic Art, Publisher's Logo (see attached)
Should not have
• Should not be AI generated

```html
<!DOCTYPE html>
<html lang="en">
<head>
<meta charset="utf-8">
<title>Lanterns &amp; Pathways of Dawn — Book Cover</title>
<link href="https://fonts.googleapis.com/css2?family=Cinzel:wght@400;500;600&family=Libre+Baskerville&family=Montserrat:wght@500;600&display=swap" rel="stylesheet">
<style>
  :root {
    --cover-blue: #0b95cb;
    --pattern-blue: #1a9dd0;
    --pale-blue: #6fccea;
    --ice: #e9f6fb;
    --white: #ffffff;
    --cream: #fbf8ef;
    --gold: #f7b955;
    --gold-deep: #b98a4e;
  }
  * { margin: 0; padding: 0; box-sizing: border-box; }
  html, body { width: 1200px; height: 880px; overflow: hidden; background: var(--cover-blue); }
  .cover { position: relative; width: 1200px; height: 880px; background: var(--cover-blue); color: var(--white); }

  /* Back cover */
  .back-title {
    position: absolute; left: 60px; top: 68px; width: 476px;
    font-family: "Cinzel", serif; font-weight: 500; font-size: 38px; line-height: 42px;
    text-align: center; letter-spacing: 0.5px;
  }
  .blurb {
    position: absolute; left: 89px; top: 214px; width: 417px;
    font-family: "Libre Baskerville", serif; font-size: 11.6px; line-height: 22px;
    text-align: justify; hyphens: auto;
  }
  .publisher {
    position: absolute; left: 102px; top: 738px; display: flex; align-items: center; gap: 14px;
  }
  .publisher-square { width: 40px; height: 40px; border: 2px solid var(--white); }
  .publisher-name {
    font-family: "Montserrat", sans-serif; font-weight: 600; font-size: 15px; line-height: 20px;
    letter-spacing: 1.5px; text-transform: uppercase;
  }

  /* Spine */
  .spine-title, .spine-author {
    position: absolute; left: 588px; writing-mode: vertical-rl; white-space: nowrap;
  }
  .spine-title { top: 74px; font-family: "Cinzel", serif; font-weight: 500; font-size: 19px; letter-spacing: 0.3px; }
  .spine-author { top: 484px; font-family: "Montserrat", sans-serif; font-weight: 500; font-size: 18px; letter-spacing: 0.8px; }

  /* Front cover */
  .front-title {
    position: absolute; left: 640px; top: 72px; width: 528px; text-align: center;
    font-family: "Cinzel", serif; font-weight: 500; font-size: 56px; line-height: 62px; letter-spacing: 1px;
  }
  .front-title-accent {
    position: absolute; left: 640px; top: 188px; width: 528px; text-align: center;
    font-family: "Cinzel", serif; font-weight: 600; font-size: 88px; line-height: 92px;
    color: var(--pale-blue); opacity: 0.75;
  }
  .names-pattern {
    position: absolute; left: 657px; top: 211px; width: 493px; height: 540px;
    background: linear-gradient(180deg, var(--pattern-blue), #1497cc);
    opacity: 0.7;
  }
  .medallion { position: absolute; left: 728px; top: 210px; width: 350px; height: 540px; }
  .front-author {
    position: absolute; left: 640px; top: 762px; width: 528px; text-align: center;
    font-family: "Montserrat", sans-serif; font-weight: 600; font-size: 30px; line-height: 36px; letter-spacing: 1.5px;
  }
</style>
</head>
<body>
<main class="cover">

  <section class="back-cover">
    <h2 class="back-title">LANTERNS &amp;<br>PATHWAYS OF DAWN</h2>
    <p class="blurb">Lorem ipsum dolor sit amet, consectetuer adipiscing elit, sed diam nonummy nibh euismod tincidunt ut laoreet dolore magna aliquam erat volutpat. Ut wisi enim ad minim veniam, quis nostrud exerci tation ullamcorper suscipit lobortis nisl ut aliquip ex ea commodo consequat. Duis autem vel eum iriure dolor in hendrerit in vulputate velit esse molestie consequat, vel illum dolore eu feugiat nulla facilisis at vero eros et accumsan et Lorem ipsum dolor sit amet, consectetuer adipiscing elit, sed diam nonummy nibh euismod tincidunt ut laoreet dolore magna aliquam erat volutpat. Ut wisi enim ad minim veniam, quis nostrud exerci tation ullamcorper suscipit lobortis nisl ut aliquip ex ea commodo consequat. Duis autem vel eum iriure dolor in hendrerit in vulputate velit esse molestie consequat, vel illum dolore eu feugiat nulla facilisis at vero eros et accumsan et Lorem ipsum dolor sit amet, consectetuer adipiscing elit, sed diam nonummy nibh euismod tincidunt ut laoreet dolore magna aliquam erat volutpat. Ut wisi enim ad minim veniam, quis nostrud exerci tation ullamcorper suscipit lobortis nisl ut aliquip ex ea commodo consequat. Duis autem vel eum iriure dolor in hendrerit in vulputate velit esse molestie consequat, vel illum dolore eu feugiat nulla facilisis at vero eros et accumsan et</p>
    <div class="publisher">
      <span class="publisher-square"></span>
      <span class="publisher-name">Qasemir Institiute<br>Australia</span>
    </div>
  </section>

  <section class="spine">
    <span class="spine-title">LANTERNS &amp; PATHWAYS OF DAWN</span>
    <span class="spine-author">AYATOLLAH KARIM MASOUDEH</span>
  </section>

  <section class="front-cover">
    <h1 class="front-title">LANTERNS &amp;<br>PATHWAYS OF</h1>
    <div class="front-title-accent">DAWN</div>
    <div class="names-pattern" role="img" aria-label="Faint grid of Arabic calligraphic divine names with small transliterations"></div>
    <svg class="medallion" viewBox="0 0 350 540" role="img" aria-label="Arched cream medallion framed in gold, holding gold Arabic calligraphy">
      <defs>
        <radialGradient id="medallion-glow" cx="50%" cy="55%" r="55%">
          <stop offset="0%" stop-color="#e9c98f"/>
          <stop offset="60%" stop-color="#f6efdf"/>
          <stop offset="100%" stop-color="#fbf8ef"/>
        </radialGradient>
      </defs>
      <path d="M175 4 C150 40 110 52 80 72 C50 92 60 140 40 170 C20 200 6 210 6 250 L6 340 C6 380 26 400 40 430 C60 470 90 480 120 500 C145 515 160 525 175 536 C190 525 205 515 230 500 C260 480 290 470 310 430 C324 400 344 380 344 340 L344 250 C344 210 330 200 310 170 C290 140 300 92 270 72 C240 52 200 40 175 4 Z"
            fill="url(#medallion-glow)" stroke="var(--gold)" stroke-width="6"/>
    </svg>
    <p class="front-author">AYATOLLAH<br>KARIM MASOUDEH</p>
  </section>

</main>
</body>
</html>
```